LES PRODUIT CONGELEES BORVALLO

we need a flyer to advertize my frozen food company titled
(LES PRODUIT CONGELEE BORVALLO) IN FROZEN LETTERS (FROSTED)
We have supplied you with identified pictures and all the menu in detail (frozen flyer)

The COVER PAGE must contain;

- My LOGO
- LIVRAISON A DOMICILE (min15$)
- pitch phrase (LES PRODUIT CONGELEE BORVALLO SON IDEAL POUR TOUT OCCASION, CAMPING, CHALET OU SIMPLEMENT UN SOUPE EN FAMILLE)
- a picture of my products (cover page pic)
- 5 nouveau produits sur notre menu
- www.borvallo-exemple.com-info@borvallo-exemple.com
- 514-555-0187
- 4871 Vaudrin Est- St-Leonard,Quebec H0X0X0

INSIDE FLYER;
- every section has a diffrent food category you must match the picture with each section

EXAMPLE; PIZZA CONGELEE must have a picture of our pizza near it.

- DO NOT write the title on every page like i did just one time on the cover page pls.

- please feel free to be creative and change the layout and font to make it more appealing

LAST PAGE AT BOTTOM;

LIVRAISON/COMPTOIR
LUNDI 11:00 -21:30 MARDI auJEUDI 11:00 - 22:00
VENDREDI et SAMEDI 11:00 - 23:00 DIMANCHE 15:00 - 21:30

Target Market(s)

everyone

Industry/Entity Type

It Company

Font styles to use
Sans Serif

Requirements
Must have
• everything i informed you with

```html
<!DOCTYPE html>
<html lang="fr">
<head>
<meta charset="utf-8">
<title>Borvallo – dépliant</title>
<link href="https://fonts.googleapis.com/css2?family=Montserrat:wght@400;600;700;800&display=swap" rel="stylesheet">
<style>
  :root{
    --red:#d3121c;
    --red-dark:#a50c12;
    --orange:#e8620f;
    --ink:#2f2f2f;
    --grey:#555;
    --paper:#f6f6f6;
    --stage:#dcdcdc;
    --logo:#3a3a3a;
    --photo-a:#c98a3c;
    --photo-b:#6e3a1c;
  }
  *{box-sizing:border-box;margin:0;padding:0}
  html,body{width:1200px;height:848px;overflow:hidden;background:var(--stage);font-family:"Montserrat",sans-serif}
  .canvas{position:relative;width:1200px;height:848px}
  .page{position:absolute;top:28px;width:560px;height:792px;background:var(--paper);overflow:hidden;box-shadow:0 6px 18px rgba(0,0,0,.18)}
  .page--front{left:30px}
  .page--back{left:610px}
  .page svg.shapes{position:absolute;inset:0;width:560px;height:792px}
  .logo{position:absolute;width:150px;height:150px;border-radius:50%;background:var(--logo);border:4px solid #fff;box-shadow:0 0 0 2px var(--logo);display:flex;align-items:center;justify-content:center;text-align:center;color:#fff;font-weight:600;font-size:15px;letter-spacing:1.5px;line-height:1.35}
  .page--front .logo{right:36px;top:96px}
  .page--back .logo{left:205px;top:262px}
  .badge{position:absolute;left:40px;top:222px;width:156px;height:156px;border-radius:50%;background:#fff;border:7px solid var(--red);box-shadow:0 0 0 4px #fff,0 0 0 7px var(--red);display:flex;flex-direction:column;align-items:center;justify-content:center;line-height:1.05}
  .badge__top{color:var(--orange);font-weight:700;font-size:15px}
  .badge__mid{color:var(--orange);font-weight:800;font-size:22px}
  .badge__min{color:#111;font-weight:800;font-size:26px}
  .thumb{position:absolute;left:200px;top:280px;width:118px;height:118px;border-radius:50%;border:6px solid #fff;box-shadow:0 0 0 3px var(--red);background:radial-gradient(circle at 40% 40%,#f0d9a0,#b9702d 70%,#6b3316)}
  .pitch{position:absolute;left:20px;right:20px;top:420px;text-align:center;font-size:22px;line-height:1.3;color:var(--ink)}
  .pitch strong{color:var(--red);font-weight:800}
  .contact{position:absolute;text-align:center;line-height:1.35}
  .page--front .contact{left:0;right:0;top:672px;color:#fff;font-size:13px;font-weight:600}
  .contact .web{letter-spacing:4px;font-size:14px}
  .hours{position:absolute;left:50px;right:50px;top:432px;border:2px solid var(--red);border-radius:14px;background:#fff;padding:12px 10px;text-align:center;font-size:12.5px;font-weight:700;color:var(--ink);line-height:1.55}
  .hours__title{color:var(--red);font-size:14px}
  .hours em{font-style:normal;color:var(--red)}
  .page--back .contact{left:0;right:0;top:548px;color:var(--ink);font-size:14px;font-weight:700}
</style>
</head>
<body>
<main class="canvas">

  <section class="page page--front">
    <svg class="shapes" viewBox="0 0 560 792" aria-hidden="false">
      <defs>
        <linearGradient id="photoFront" x1="0" y1="0" x2="1" y2="1">
          <stop offset="0" stop-color="var(--photo-a)"/><stop offset="1" stop-color="var(--photo-b)"/>
        </linearGradient>
        <linearGradient id="redBand" x1="0" y1="0" x2="0" y2="1">
          <stop offset="0" stop-color="var(--red)"/><stop offset="1" stop-color="var(--red-dark)"/>
        </linearGradient>
      </defs>
      <path d="M0 0 H560 V300 C420 350 230 330 0 230 Z" fill="url(#photoFront)" role="img" aria-label="Photo d'une pizza congelée au fromage et aux épinards"/>
      <path d="M0 0 H150 C90 40 40 80 0 120 Z" fill="var(--red)"/>
      <path d="M0 230 C230 330 420 350 560 300 V316 C420 366 230 348 0 250 Z" fill="var(--red)"/>
      <path d="M180 330 C330 372 460 360 560 326 V346 C460 384 320 392 180 346 Z" fill="var(--orange)"/>
      <path d="M0 640 C130 600 240 605 300 650 C360 615 460 625 560 655 V792 H0 Z" fill="url(#redBand)"/>
    </svg>
    <div class="logo">RISTORANTE<br>BORVALLO</div>
    <div class="badge">
      <span class="badge__top">LIVRAISON A</span>
      <span class="badge__mid">DOMICILE</span>
      <span class="badge__min">MIN15$</span>
    </div>
    <div class="thumb" role="img" aria-label="Photo d'une part de pizza"></div>
    <p class="pitch">Les aliment congelee Borvallo<br><strong>son ideal pour tout occasion,</strong><br>camping, au chalet ou simplement<br><strong>un soupe en famille</strong></p>
    <address class="contact">
      Email:info@borvallo-exemple.com<br>
      4871 Vaudrin Est- St-Leonard,Quebec H0X0X0<br>
      <span class="web">www.borvallo-exemple.com</span>
    </address>
  </section>

  <section class="page page--back">
    <svg class="shapes" viewBox="0 0 560 792">
      <defs>
        <linearGradient id="photoBack" x1="0" y1="0" x2="1" y2="1">
          <stop offset="0" stop-color="#d9a452"/><stop offset="1" stop-color="var(--photo-b)"/>
        </linearGradient>
        <linearGradient id="redBand2" x1="0" y1="0" x2="0" y2="1">
          <stop offset="0" stop-color="var(--red)"/><stop offset="1" stop-color="var(--red-dark)"/>
        </linearGradient>
      </defs>
      <path d="M0 0 H560 V270 C400 280 220 230 0 130 Z" fill="url(#photoBack)" role="img" aria-label="Photo de deux pizzas congelées"/>
      <path d="M0 130 C220 230 400 280 560 270 V284 C400 294 220 246 0 146 Z" fill="var(--red)"/>
      <path d="M0 160 C200 250 360 282 420 286 C340 290 200 264 0 178 Z" fill="var(--orange)"/>
      <path d="M0 660 C180 640 300 640 330 675 C380 690 470 690 560 680 V792 H0 Z" fill="url(#redBand2)"/>
    </svg>
    <div class="logo">RISTORANTE<br>BORVALLO</div>
    <div class="hours">
      <div class="hours__title">LIVRAISON/COMPTOIR</div>
      LUNDI <em>11:00 -21:30</em> ,MARDI auJEUDI <em>11:00 - 22:00</em><br>
      VENDREDI et SAMEDI 11:00 - 23:00 DIMANCHE 15:00 - 21:30
    </div>
    <address class="contact">
      Email:info@borvallo-exemple.com<br>
      4871 Vaudrin Est- St-Leonard,Quebec H0X0X0<br>
      <span class="web">www.borvallo-exemple.com</span>
    </address>
  </section>

</main>
</body>
</html>
```